依頼概要
■依頼の目的/概要
コンサルティング業の中で「ほたる相談室」というテーマの中で、
営業力や対人対応力の向上支援などをお手伝いしています。
今回電子書籍出版にあたり、添付ファイルの書籍のイメージに沿うデザインを製作依頼させていただきます。

■書籍タイトル:『どうして?腕時計を磨くと来店客がふえるのか』
サブタイトル:「未来をひらくのは話術より笑顔力」

■本の内容
見た目が人に与える印象などについて記載したものになります。
営業マンのような個人の方や、法人教育に携わるような方にもお読みいただきたいものです。
詳細は添付ファイルを参照ください。

■デザイン要望
自由なご提案をおまちしております。
堅苦しくなく、気軽に手に取っていただけるようなデザインを希望です。

その他何かご不明な点がございましたら、お気軽にご質問下さい。
よろしくお願いいたします。
提案して頂いた皆様、私のミスで写真を2枚お送りできていませんでした。
大変申し訳ございませんがこの写真2枚を使って頂けますよう宜しくお願い致します。

この写真を使ってください
■ 選んだ理由

ネクタイの縦とメッセージの流れがとても良かったです。

■ 提案者全員のお礼・コメント

今回は、沢山の人にいろいろなデザインでご提案いただきありがとうございました。

```html
<!DOCTYPE html>
<html lang="ja">
<head>
<meta charset="utf-8">
<title>どうして?腕時計を磨くと来店客がふえるのか</title>
<link href="https://fonts.googleapis.com/css2?family=Noto+Serif+JP:wght@900&family=Noto+Sans+JP:wght@700;900&display=swap" rel="stylesheet">
<style>
  :root {
    --paper: #fbf8f2;
    --ink: #1a1a1a;
    --accent-red: #d81e2a;
    --accent-blue: #1e6fd0;
    --pale-blue: #d9ecff;
    --gift-pink: #ff4f9a;
    --suit-light: #b8b8b8;
    --suit-dark: #262626;
    --label-bg: rgba(255,255,255,0.88);
  }
  html, body { margin: 0; padding: 0; overflow: hidden; }
  body { width: 750px; height: 1200px; background: var(--paper); }
  .cover {
    position: relative; width: 750px; height: 1200px; overflow: hidden;
    background: var(--paper);
    font-family: "Noto Sans JP", sans-serif;
  }
  .cover h1, .cover h2, .cover p { margin: 0; }
  .suit-photo {
    position: absolute; left: 0; top: 520px; width: 750px; height: 680px;
    background: linear-gradient(180deg, var(--paper) 0%, #d8d8d8 12%, var(--suit-light) 28%, #6a6a6a 60%, var(--suit-dark) 100%);
  }
  .author-photo {
    position: absolute; left: 566px; top: 478px; width: 184px; height: 200px;
    background: linear-gradient(160deg, #efefef 0%, #b9b4ad 45%, #4a4746 100%);
  }
  .title-col {
    position: absolute; top: 24px;
    writing-mode: vertical-rl;
    font-family: "Noto Serif JP", serif; font-weight: 900;
    font-size: 86px; line-height: 1; letter-spacing: 2px;
    color: var(--ink);
  }
  .title-col.red { color: var(--accent-red); }
  .author-name {
    position: absolute; left: 500px; top: 686px;
    font-size: 34px; font-weight: 900; line-height: 1.2; color: var(--ink);
    background: var(--label-bg); padding: 4px 8px;
  }
  .author-name small { font-size: 18px; margin-left: 6px; }
  .author-role {
    position: absolute; left: 706px; top: 686px;
    writing-mode: vertical-rl;
    font-size: 22px; font-weight: 700; line-height: 1; color: var(--ink);
    background: var(--label-bg); padding: 6px 5px;
  }
  .tag-col {
    position: absolute;
    writing-mode: vertical-rl;
    font-weight: 900; line-height: 1;
  }
  .tag-lead { left: 430px; top: 630px; font-size: 52px; color: var(--pale-blue); -webkit-text-stroke: 1px var(--accent-blue); }
  .tag-mid { left: 368px; top: 660px; font-size: 52px; color: var(--pale-blue); -webkit-text-stroke: 1px var(--accent-blue); }
  .tag-key { left: 268px; top: 636px; font-size: 82px; color: var(--accent-blue); -webkit-text-stroke: 2px #ffffff; }
  .gift { position: absolute; left: 22px; width: 270px; }
  .gift-label { font-size: 22px; font-weight: 900; color: var(--gift-pink); margin-bottom: 6px !important; }
  .gift-body {
    background: var(--label-bg); color: var(--ink);
    font-size: 21px; font-weight: 700; line-height: 1.4;
    padding: 8px 12px;
  }
  .gift-one { top: 930px; }
  .gift-two { top: 1050px; }
</style>
</head>
<body>
<div class="cover">
  <div class="suit-photo" role="img" aria-label="スーツとネクタイを締めた胸元の写真"></div>
  <div class="author-photo" role="img" aria-label="著者の写真"></div>

  <h1 class="book-title">
    <span class="title-col" style="left:640px">どうして？</span>
    <span class="title-col red" style="left:530px">腕時計を</span>
    <span class="title-col red" style="left:420px">磨くと</span>
    <span class="title-col" style="left:298px">来店客が</span>
    <span class="title-col" style="left:180px">ふえるのか</span>
  </h1>

  <p class="author-name">朝霧光一<small>著</small></p>
  <p class="author-role">「ほたる相談室コンサルタント」</p>

  <h2 class="tagline">
    <span class="tag-col tag-lead">未来をひらくのは</span>
    <span class="tag-col tag-mid">話術より</span>
    <span class="tag-col tag-key">笑顔力</span>
  </h2>

  <section class="gift gift-one">
    <p class="gift-label">《読者プレゼント①》</p>
    <p class="gift-body">得たい成果を得る為の<br>5つのステップ!</p>
  </section>
  <section class="gift gift-two">
    <p class="gift-label">《読者プレゼント②》</p>
    <p class="gift-body">失敗しないもの選び・<br>マスコミでは出さない<br>もの選びのポイント!</p>
  </section>
</div>
</body>
</html>
```